Digital agency needs a new web design

We’re looking to redesign our website – so that it is 3 things: smart, stylish and simplistic.
Plenix are a digital performance agency, offering services in PPC. SEO. Analytics, Display, Content and Paid Social, and we work with fantastic clients.
Our current website isn't reflective of how forward-thinking we are as an agency, and doesn't convey our two USPs well - our technology and our network of digital marketing experts. So we're looking to build a clear and concise site that attracts both inbound leads and digital marketing professionals to join our team or our Plenixer network.
You can take a look at our current website here - http://plenix-example.com/. The copy will change and we happy for the colours to change.

Target Market(s)

The primary target audience is marketing directors, digital directors, marketing managers and online acquisition managers. The secondary audience are people in the industry looking for work either as permanent employees or as part of the Plenix freelance network.

Industry/Entity Type

Marketing

Number of Pages Required

5+ page

Font styles to use
Sans Serif

Requirements
Must have
• - A stylish/ grown-up feel
• - Be of a design/ templates that can be editable
• - A really clear concise/ homepage
• The homepage must include:
• 1. A reference to our services
• 2. A reference to our network of digital marketing experts
• 3. A reference to our technology
• 4. A section for case studies
• 5. A section for our blog
• 6. A newsletter signup
• Th copy will be changed so please don't feel like you need to keep that.
Should not have
• - Cartoon style images as on the site on the moment
• - You should not have to scroll very far to find out what we do

```html
<!DOCTYPE html>
<html lang="en">
<head>
<meta charset="utf-8">
<title>Plenix — Digital Performance Re-invented</title>
<link rel="stylesheet" href="https://fonts.googleapis.com/css2?family=Open+Sans:wght@400;600;700&display=swap">
<style>
:root{
  --yellow:#f6c500;
  --ink:#2a2a2a;
  --white:#ffffff;
  --grey:#666666;
  --light:#f3f3f3;
  --footer:#2c2c2c;
  --footer-text:#bdbdbd;
}
*{margin:0;padding:0;box-sizing:border-box}
html,body{width:1200px;height:2496px;overflow:hidden;background:var(--white)}
body{font-family:"Open Sans",Arial,sans-serif;color:var(--ink);position:relative}

.hero{position:absolute;left:0;top:0;width:1200px;height:580px;
  background:linear-gradient(180deg,#3b3f44 0%,#5a5e63 40%,#4a4c50 75%,#2e3034 100%)}
.brand{position:absolute;left:28px;top:24px;display:flex;align-items:center;gap:10px;color:var(--white);font-weight:600;font-size:26px}
.brand .dot{width:16px;height:16px;border-radius:50%;background:var(--white)}
.menu{position:absolute;right:28px;top:30px;color:var(--white);font-size:14px;font-weight:600;display:flex;align-items:center;gap:10px;letter-spacing:1px}
.menu svg{display:block}
.hero h1{position:absolute;top:202px;width:100%;text-align:center;color:var(--white);font-weight:400;font-size:46px;letter-spacing:1px}
.hero .services{position:absolute;top:264px;width:100%;text-align:center;color:var(--yellow);font-size:22px;font-weight:600;letter-spacing:1px}
.video{position:absolute;left:440px;top:320px;width:320px;height:160px;background:linear-gradient(135deg,#3a3a3a,#6b6b6b 55%,#2f2f2f)}
.video svg{position:absolute;left:140px;top:60px}

.solutions{position:absolute;left:0;top:580px;width:1200px;height:220px;background:var(--yellow);text-align:center}
.solutions h2{margin-top:84px;color:var(--white);font-size:44px;font-weight:700;letter-spacing:1px}
.solutions p{margin-top:8px;color:var(--white);font-size:19px}

.grid{position:absolute;left:0;top:800px;width:1200px;height:580px;display:grid;grid-template-columns:repeat(3,400px);grid-template-rows:repeat(2,290px)}
.tile{position:relative;text-align:center;padding-top:52px}
.tile:nth-child(1){background:linear-gradient(160deg,#4a4a4a,#202020)}
.tile:nth-child(2){background:linear-gradient(160deg,#5c5c5c,#2c2c2c)}
.tile:nth-child(3){background:linear-gradient(160deg,#3c3c3c,#1c1c1c)}
.tile:nth-child(4){background:linear-gradient(160deg,#505050,#262626)}
.tile:nth-child(5){background:linear-gradient(160deg,#444,#1e1e1e)}
.tile:nth-child(6){background:linear-gradient(160deg,#585858,#2a2a2a)}
.tile h3{font-size:40px;font-weight:700;color:var(--white)}
.tile.accent h3{color:var(--yellow)}
.tile p{width:220px;margin:14px auto 0;font-size:14px;line-height:20px;color:var(--yellow)}
.tile.accent p{color:var(--white)}
.btn{display:inline-block;margin-top:22px;border:2px solid var(--white);color:var(--white);font-size:15px;font-weight:600;padding:7px 18px;letter-spacing:1px}
.tile.accent .btn{border-color:var(--yellow)}

.explore{position:absolute;left:0;top:1380px;width:1200px;height:132px;background:var(--yellow);text-align:center}
.explore .btn{margin-top:40px;padding:12px 26px;font-size:17px}

.clients{position:absolute;left:0;top:1512px;width:1200px;height:460px;text-align:center}
.clients h2{margin-top:40px;font-size:44px;font-weight:700;color:var(--ink);letter-spacing:1px}
.clients p{width:680px;margin:14px auto 0;color:var(--yellow);font-size:19px;line-height:28px}
.client-list{position:absolute;left:60px;top:196px;width:1080px;display:grid;grid-template-columns:repeat(4,270px);grid-auto-rows:64px;align-items:center}
.client{font-size:21px;font-weight:600;color:#333;text-align:center}
.client:nth-child(4n+1){text-align:left}
.client:nth-child(4n){text-align:right}

.highlights{position:absolute;left:0;top:1972px;width:1200px;height:188px;background:var(--light);
  display:grid;grid-template-columns:repeat(4,1fr);column-gap:40px;padding:34px 60px 0}
.highlight{border-top:3px solid var(--yellow);padding-top:14px}
.highlight h3{font-size:18px;font-weight:700;color:var(--ink);letter-spacing:1px}
.highlight p{margin-top:6px;font-size:14px;line-height:20px;color:var(--grey)}
.highlight .more{display:inline-block;margin-top:8px;font-size:13px;font-weight:600;color:var(--yellow);letter-spacing:1px}

.footer{position:absolute;left:0;top:2160px;width:1200px;height:336px;background:var(--footer);color:var(--footer-text);font-size:16px;line-height:30px}
.col{position:absolute;top:22px}
.col h4{color:var(--yellow);font-size:15px;font-weight:600;letter-spacing:2px;margin-bottom:18px}
.col.contact{left:60px}.col.pages{left:368px}.col.links{left:680px}
.col .gap{height:18px}
.brand-foot{position:absolute;right:60px;top:22px;text-align:right;color:var(--footer-text)}
.brand-foot .name{display:inline-flex;align-items:center;gap:8px;color:var(--white);font-weight:600;font-size:24px;margin-bottom:8px}
.brand-foot .dot{width:12px;height:12px;border-radius:50%;background:var(--white)}
.newsletter{position:absolute;right:60px;top:150px;width:300px}
.newsletter h4{color:var(--yellow);font-size:15px;font-weight:600;letter-spacing:2px;margin-bottom:10px;text-align:right}
.signup{display:flex;height:40px}
.signup .field{flex:1;border:1px solid #5a5a5a;color:#8a8a8a;font-size:14px;line-height:38px;padding:0 12px}
.signup .submit{background:var(--yellow);color:var(--ink);font-size:13px;font-weight:700;letter-spacing:1px;line-height:40px;padding:0 16px}
</style>
</head>
<body>
<header class="hero" role="img" aria-label="Night-time city skyline photograph with overlaid network lines">
  <div class="brand"><span class="dot"></span>plenix</div>
  <div class="menu">MENU
    <svg width="22" height="16" viewBox="0 0 22 16"><rect y="0" width="22" height="2" fill="#fff"/><rect y="7" width="22" height="2" fill="#fff"/><rect y="14" width="22" height="2" fill="#fff"/></svg>
  </div>
  <h1>DIGITAL PERFORMANCE RE-INVENTED</h1>
  <div class="services">PPC - DISPLAY - PAID SOCIAL - SEO - CONTENT - ANALYTICS</div>
  <div class="video" role="img" aria-label="Video still of a presenter speaking to camera">
    <svg width="40" height="40" viewBox="0 0 40 40"><circle cx="20" cy="20" r="20" fill="#f6c500"/><path d="M15 11 L29 20 L15 29 Z" fill="#2a2a2a"/></svg>
  </div>
</header>

<section class="solutions">
  <h2>SOLUTIONS</h2>
  <p>Your business goal converts into our business goals</p>
</section>

<section class="grid">
  <article class="tile" role="img" aria-label="Dark photo of a search dashboard"><h3>PPC</h3><p>Smart campaigns built on data and run by experts.</p><span class="btn">READ MORE</span></article>
  <article class="tile accent" role="img" aria-label="Dark photo of analytics charts"><h3>ANALYTICS</h3><p>Smart campaigns built on data and run by experts.</p><span class="btn">READ MORE</span></article>
  <article class="tile" role="img" aria-label="Dark photo of a keyboard"><h3>SEO</h3><p>Smart campaigns built on data and run by experts.</p><span class="btn">READ MORE</span></article>
  <article class="tile accent" role="img" aria-label="Dark photo of display screens"><h3>DISPLAY</h3><p>Smart campaigns built on data and run by experts.</p><span class="btn">READ MORE</span></article>
  <article class="tile" role="img" aria-label="Dark photo of social media on a phone"><h3>PAID SOCIAL</h3><p>Smart campaigns built on data and run by experts.</p><span class="btn">READ MORE</span></article>
  <article class="tile accent" role="img" aria-label="Dark photo of printed articles"><h3>CONTENT</h3><p>Smart campaigns built on data and run by experts.</p><span class="btn">READ MORE</span></article>
</section>

<section class="explore"><span class="btn">EXPLORE ALL</span></section>

<section class="clients">
  <h2>WHO WE WORK WITH</h2>
  <p>We want to build good &amp; trustworthy relationships with our clients &amp; we believe that's the only way to achieve success.</p>
  <div class="client-list">
    <span class="client">Nortavo</span><span class="client">Brightleaf</span><span class="client">The Mutual Harbour Bank</span><span class="client">RoadAid</span>
    <span class="client">Granmoor</span><span class="client">Hartley &amp; Finch</span><span class="client">The Daily Ledger</span><span class="client">Vantrell</span>
    <span class="client">Pacewell</span><span class="client">Carden Bros.</span><span class="client">Keystone Cover</span><span class="client">Talent Page</span>
    <span class="client">glowlane.com</span><span class="client">Orbis TV</span><span class="client">rootseeker</span><span class="client">Harlow Vale</span>
  </div>
</section>

<section class="highlights">
  <article class="highlight"><h3>OUR NETWORK</h3><p>Over 1,000 Plenixers, digital experts ready to work in any market.</p><span class="more">JOIN THE NETWORK →</span></article>
  <article class="highlight"><h3>OUR TECHNOLOGY</h3><p>Our own platform links every campaign, expert and result in one place.</p><span class="more">SEE THE TECH →</span></article>
  <article class="highlight"><h3>CASE STUDIES</h3><p>Real growth for real brands, measured and shared in detail.</p><span class="more">VIEW CASE STUDIES →</span></article>
  <article class="highlight"><h3>BLOG</h3><p>Fresh thinking on search, social and performance marketing.</p><span class="more">READ THE BLOG →</span></article>
</section>

<footer class="footer">
  <div class="col contact"><h4>CONTACT</h4>+44 20 0000 1234<div class="gap"></div>London<br>New York<br>Sydney<br>Shrewsbury</div>
  <div class="col pages"><h4>PAGES</h4>Services<br>Team<br>Tech<br>Blog<br>Career<br>Contact</div>
  <div class="col links"><h4>LINKS</h4>Newsfeed<br>Chirper<br>Circles<br>ProLink</div>
  <div class="brand-foot"><span class="name"><span class="dot"></span>plenix</span><br>Copyright 2016<br>All Rights reserved</div>
  <form class="newsletter">
    <h4>NEWSLETTER</h4>
    <div class="signup"><span class="field">Your email address</span><span class="submit">SIGN UP</span></div>
  </form>
</footer>
</body>
</html>
```